Bloom and Rise Website Design (design layout only)

We need a website design for a new nonprofit organization based in Des Moines, Iowa called Bloom and Rise. The nonprofit provides soccer training opportunities to youth soccer players looking to improve their game while also affecting the lives of the less fortunate in a positive way. While participating in the training programs the players also go out and raise money for selected charities. The organization then donates the funds. In its first 18 months we donated $10,500. We would like to see designs attempt to symbolize the mission of the nonprofit - essentially "improve you while improving someone else."

We would like to see the following features:

· A place to donate - Our intent is to have the home page linked to the donation page; a simple straight-forward process for people to give money, and make donating as painless as possible - no account needed to make a donation, credit card or e-check should be the only information needed to donate, and have it be on a single page.

· A photo gallery so people can browse the photo gallery to get a better understanding of our organization and a place to add videos and a calendar to show upcoming events

· A place for contact information and the profiles of directors and board members. This should include a spot showing all the charities the organization donates to. Also includes a news section/blog for comments and suggestions.

We want the design to revolve around the content and mission. We would really like to stress our organization as nonprofit. We would also like if the website was user friendly and easy to navigate.

The logo of our organization is uploaded

```html
<!DOCTYPE html>
<html lang="en">
<head>
<meta charset="utf-8">
<title>Bloom and Rise</title>
<link href="https://fonts.googleapis.com/css2?family=Arimo:wght@400;700&display=swap" rel="stylesheet">
<style>
:root{
  --green-dark:#4a6530;
  --green-bright:#7db52e;
  --green-text:#4f7a25;
  --green-light:#b9d68c;
  --ink:#444;
  --muted:#888;
  --rule:#dcdcdc;
  --paper:#fff;
  --mist:#f6f6f6;
  --footer:#343434;
}
*{margin:0;padding:0;box-sizing:border-box}
html,body{width:968px;height:1200px;overflow:hidden}
body{position:relative;font-family:"Arimo",Arial,sans-serif;color:var(--ink);background:var(--paper)}
.abs{position:absolute}
.photo{position:absolute;border-radius:2px}

/* header */
.site-header{position:absolute;left:0;top:0;width:968px;height:54px;background:var(--paper)}
.brand{left:192px;top:14px;display:flex;align-items:center;gap:8px}
.brand-mark{width:22px;height:22px;background:var(--green-bright)}
.brand-name{font-size:18px;font-weight:700;color:var(--green-text);letter-spacing:.3px;white-space:nowrap}
.nav{right:208px;top:20px;display:flex;gap:18px;font-size:7.5px;color:var(--muted);text-transform:uppercase;align-items:center;white-space:nowrap}
.nav .donate{background:var(--green-dark);color:#fff;font-weight:700;padding:5px 14px;border-bottom:3px solid var(--green-bright)}

/* hero */
.hero{left:0;top:54px;width:968px;height:264px;background:linear-gradient(100deg,#6d6a55 0%,#9c977c 35%,#c9c3a3 55%,#6e7a5a 75%,#2f5a2c 100%)}
.hero-title{left:0;top:150px;width:968px;text-align:center;color:#fff;font-size:25px;line-height:29px;font-weight:400}
.hero-sub{left:0;top:222px;width:968px;text-align:center;color:#fff;font-size:10px}

/* donation band */
.donate-band{left:0;top:318px;width:968px;height:72px;background:var(--green-dark)}
.donate-band p{position:absolute;top:14px;width:100%;text-align:center;color:#fff;font-size:9px}
.donate-btn{left:426px;top:32px;width:98px;height:26px;background:var(--green-bright);color:#fff;font-size:10px;display:flex;align-items:center;justify-content:center;gap:8px;border-radius:2px}
.donate-btn svg{width:12px;height:12px}

/* info row */
.col-title{font-size:13px;color:var(--green-text);font-weight:400}
.small{font-size:6.5px;line-height:9px;color:var(--muted)}
.event{display:flex;gap:10px;width:150px}
.event-date{width:24px;text-align:center;color:var(--muted);flex:none}
.event-date b{display:block;font-size:13px;font-weight:400;background:#f0f0f0;padding:2px 0}
.event-date span{font-size:6.5px}
.event h4{font-size:8px;font-weight:400;color:#666;margin-bottom:3px}

/* gallery */
.mist{left:0;top:540px;width:968px;height:300px;background:var(--mist)}
.card-title{width:125px;text-align:center;font-size:8.5px;color:#555;border-bottom:1px solid var(--rule);padding-bottom:6px}
.card-text{width:125px;text-align:center;font-size:6px;letter-spacing:-.15px;white-space:nowrap;color:var(--muted)}
.read-more{width:125px;text-align:center;font-size:5.5px;color:#666;text-decoration:underline}
.blog-title{font-size:9.5px;color:#777;line-height:11px;width:90px}
.blog-date{font-size:6.5px;color:var(--green-text)}
.blog-meta{font-size:5.5px;line-height:7px;color:var(--muted)}

/* board */
.board{left:0;top:840px;width:968px;height:174px;background:var(--green-dark);color:#fff}
.board-title{color:var(--green-light);font-size:13px;font-weight:400}
.member-name{font-size:8px;width:118px;border-bottom:1px solid #7c9262;padding-bottom:6px}
.avatar{width:36px;height:36px;border-radius:50%;background:linear-gradient(#d9c6b4,#8a7a6c)}
.member-text{font-size:6.5px;line-height:8.5px;width:78px}
.fee{width:118px;font-size:7px;display:flex;justify-content:space-between;border-top:1px solid #7c9262;padding-top:5px;line-height:13px;flex-wrap:wrap}
.fee span{width:50%}
.fee span:nth-child(even){text-align:right}

/* footer */
.footer{left:0;top:1014px;width:968px;height:186px;background:var(--footer);color:#ddd}
.footer h5{font-size:9px;font-weight:400;color:#eee}
.foot-brand{font-size:15px;font-weight:700;color:#ddd}
.foot-text{font-size:6px;line-height:9px;font-style:italic;color:#ccc;width:150px}
.foot-menu{list-style:none;font-size:6.5px;line-height:11.5px;color:#ccc}
.news-item{display:flex;gap:8px;width:180px;margin-bottom:8px}
.news-thumb{width:46px;height:30px;background:linear-gradient(#cfcfcf,#7a7a7a);flex:none}
.news-item p{font-size:6.5px;line-height:8.5px;color:#ccc}
.news-item small{display:block;margin-top:3px;font-size:6px}
.social{display:flex;gap:10px}
.social span{width:8px;height:8px;border-radius:50%;background:#ccc}
</style>
</head>
<body>

<header class="site-header">
  <div class="abs brand"><span class="brand-mark"></span><span class="brand-name">Bloom and Rise</span></div>
  <nav class="abs nav"><span>Home</span><span>About Us</span><span>Blogs</span><span>Custom Link</span><span class="donate">Donate</span><span>Contact Us</span></nav>
</header>

<section class="abs hero" role="img" aria-label="Photo of two youth soccer players challenging for the ball on a muddy field"></section>
<h1 class="abs hero-title">nonprofit provides soccer<br>training opportunities</h1>
<p class="abs hero-sub">improve you while improving someone else</p>

<section class="abs donate-band">
  <p>You can be a hero by Giving a small donation. Also you can track where you donation goes</p>
  <div class="abs donate-btn">DONATE NOW
    <svg viewBox="0 0 12 12"><circle cx="6" cy="6" r="6" fill="#4a6530"/><path d="M5 3.5 7.5 6 5 8.5" stroke="#fff" stroke-width="1.4" fill="none"/></svg>
  </div>
</section>

<!-- info row -->
<h2 class="abs col-title" style="left:192px;top:413px">Upcoming</h2>
<p class="abs small" style="left:192px;top:435px;width:160px">Lorem Ipsum is simply dummy text of the printing and typesetting industry. Lorem Ipsum has been the industry's standard Lorem Ipsum is simply dummy text of the printing</p>

<h2 class="abs col-title" style="left:391px;top:413px">Next Event</h2>
<div class="abs event" style="left:391px;top:434px">
  <div class="event-date"><b>04</b><span>AUG</span></div>
  <div><h4>Upcoming Heading Here</h4><p class="small">Lorem Ipsum is simply dummy text printing and typesetting industry. Lorem Ipsum has been</p></div>
</div>
<div class="abs" style="left:391px;top:478px;width:152px;border-top:1px solid var(--rule)"></div>
<div class="abs event" style="left:391px;top:486px">
  <div class="event-date"><b>06</b><span>AUG</span></div>
  <div><h4>Upcoming Heading Here</h4><p class="small">Lorem Ipsum is simply dummy text printing and typesetting industry. Lorem Ipsum has been</p></div>
</div>

<h2 class="abs col-title" style="left:590px;top:413px">Featured Video</h2>
<div class="photo" style="left:590px;top:433px;width:170px;height:89px;background:linear-gradient(120deg,#7b7a70,#c9b99a 50%,#3f6b3a)" role="img" aria-label="Video still of a player striking the ball"></div>
<div class="abs" style="left:590px;top:508px;width:170px;height:14px;background:#111"></div>
<svg class="abs" style="left:596px;top:511px" width="160" height="8" viewBox="0 0 160 8"><path d="M0 0 6 4 0 8z" fill="#fff"/><rect x="18" y="3" width="100" height="2" fill="#555"/><rect x="128" y="3" width="20" height="2" fill="#3b8de0"/></svg>
<svg class="abs" style="left:662px;top:463px" width="22" height="22" viewBox="0 0 22 22"><circle cx="11" cy="11" r="11" fill="#fff" opacity=".85"/><path d="M8.5 6.5 15.5 11 8.5 15.5z" fill="#333"/></svg>

<!-- gallery -->
<section class="abs mist"></section>
<h2 class="abs col-title" style="left:192px;top:554px">Gallery</h2>
<div class="photo" style="left:192px;top:576px;width:125px;height:77px;background:linear-gradient(#3a8ad0,#7bb3d8 55%,#3e8a33)" role="img" aria-label="Player kicking a ball on a grass pitch under blue sky"></div>
<div class="photo" style="left:340px;top:576px;width:125px;height:77px;background:linear-gradient(120deg,#2a2520,#8a7a66 55%,#3a332c)" role="img" aria-label="Two players competing in a header"></div>
<div class="photo" style="left:490px;top:576px;width:125px;height:77px;background:radial-gradient(circle at 50% 40%,#e06a1a,#8a2a0c 60%,#2a0e06)" role="img" aria-label="Player in orange jumping against a fiery sky"></div>
<div class="photo" style="left:635px;top:576px;width:125px;height:77px;background:linear-gradient(110deg,#bdb69a,#d8cfb2 50%,#3d6e37)" role="img" aria-label="Player sliding into a tackle on a muddy pitch"></div>

<div class="abs card-title" style="left:192px;top:662px">HEADLINE GOES HERE</div>
<div class="abs card-title" style="left:340px;top:662px">HEADLINE GOES HERE</div>
<div class="abs card-title" style="left:490px;top:662px">HEADLINE GOES HERE</div>
<div class="abs card-title" style="left:635px;top:662px">HEADLINE GOES HERE</div>
<p class="abs card-text" style="left:192px;top:687px">Lorem Ipsum is simply dummy text of the printing</p>
<p class="abs card-text" style="left:340px;top:687px">Lorem Ipsum is simply dummy text of the printing</p>
<p class="abs card-text" style="left:490px;top:687px">Lorem Ipsum is simply dummy text of the printing</p>
<p class="abs card-text" style="left:635px;top:687px">Lorem Ipsum is simply dummy text of the printing</p>
<span class="abs read-more" style="left:192px;top:700px">READ MORE</span>
<span class="abs read-more" style="left:340px;top:700px">READ MORE</span>
<span class="abs read-more" style="left:490px;top:700px">READ MORE</span>
<span class="abs read-more" style="left:635px;top:700px">READ MORE</span>

<div class="abs" style="left:192px;top:727px;width:568px;border-top:1px solid var(--rule)"></div>
<h2 class="abs col-title" style="left:192px;top:743px;color:#4a6b2a">Our Blogs Recent Post</h2>

<div class="photo" style="left:192px;top:769px;width:82px;height:48px;background:linear-gradient(90deg,#222,#8a8a8a 50%,#333)" role="img" aria-label="Street scene at night"></div>
<p class="abs blog-title" style="left:282px;top:768px">Lorem Ipsum is simply dummy text</p>
<p class="abs blog-date" style="left:282px;top:792px">August 7,2014</p>
<p class="abs blog-meta" style="left:282px;top:804px">Posted By Admin<br>0 Comments</p>

<div class="photo" style="left:390px;top:769px;width:82px;height:48px;background:linear-gradient(90deg,#4a3428,#b58a6c 50%,#3a2a22)" role="img" aria-label="Two friends wearing sunglasses"></div>
<p class="abs blog-title" style="left:480px;top:768px">Lorem Ipsum is simply dummy text</p>
<p class="abs blog-date" style="left:480px;top:792px">August 7,2014</p>
<p class="abs blog-meta" style="left:480px;top:804px">Posted By Admin<br>0 Comments</p>

<div class="photo" style="left:584px;top:769px;width:82px;height:48px;background:linear-gradient(90deg,#5a3a26,#c8b79e 55%,#6a4a30)" role="img" aria-label="Glass on a wooden table"></div>
<p class="abs blog-title" style="left:674px;top:768px">Lorem Ipsum is simply dummy text</p>
<p class="abs blog-date" style="left:674px;top:792px">August 7,2014</p>
<p class="abs blog-meta" style="left:674px;top:804px">Posted By Admin<br>0 Comments</p>

<!-- board members -->
<section class="abs board">
  <h2 class="abs board-title" style="left:192px;top:16px">Board Members</h2>

  <div class="abs member-name" style="left:192px;top:43px">Northwind Studio</div>
  <div class="abs avatar" style="left:192px;top:67px" role="img" aria-label="Portrait of board member"></div>
  <p class="abs member-text" style="left:234px;top:68px">Lorem Ipsum is simply dummy text of the printing and type-setting industry. Lorem Ipsum has</p>
  <div class="abs fee" style="left:192px;top:110px"><span>Lorem Ipsum</span><span>$300</span><span>Lorempsum</span><span>$320</span></div>

  <div class="abs member-name" style="left:343px;top:43px">Northwind</div>
  <div class="abs avatar" style="left:343px;top:67px" role="img" aria-label="Portrait of board member"></div>
  <p class="abs member-text" style="left:385px;top:68px">Lorem Ipsum is simply dummy text of the printing and type-setting industry. Lorem Ipsum has</p>
  <div class="abs fee" style="left:343px;top:110px"><span>Lorem Ipsum</span><span>$300</span><span>Lorempsum</span><span>$320</span></div>

  <div class="abs member-name" style="left:496px;top:43px">Northwind Studio</div>
  <div class="abs avatar" style="left:496px;top:67px" role="img" aria-label="Portrait of board member"></div>
  <p class="abs member-text" style="left:538px;top:68px">Lorem Ipsum is simply dummy text of the printing and type-setting industry. Lorem Ipsum has</p>
  <div class="abs fee" style="left:496px;top:110px"><span>Lorem Ipsum</span><span>$300</span><span>Lorempsum</span><span>$320</span></div>

  <div class="abs member-name" style="left:641px;top:43px">Northwind Studio</div>
  <div class="abs avatar" style="left:641px;top:67px" role="img" aria-label="Portrait of board member"></div>
  <p class="abs member-text" style="left:683px;top:68px">Lorem Ipsum is simply dummy text of the printing and type-setting industry. Lorem Ipsum has</p>
  <div class="abs fee" style="left:641px;top:110px"><span>Lorem Ipsum</span><span>$300</span><span>Lorempsum</span><span>$320</span></div>
</section>

<!-- footer -->
<footer class="abs footer">
  <div class="abs foot-brand" style="left:192px;top:42px">Bloom and Rise</div>
  <p class="abs foot-text" style="left:192px;top:66px">Lorem Ipsum is simply dummy text of the printing and typesetting industry. Lorem Ipsum has been the industry's standard dummy text ever since the 1500s, when an unknown printer took a galley of type and scrambled it to make a type specimen book. It has survived not only five centuries, but also the leap into electronic typesetting, remaining essentially unchanged.</p>
  <p class="abs" style="left:192px;top:146px;font-size:5.5px;color:#bbb">Copyright All Right Reserved 2014</p>

  <h5 class="abs" style="left:389px;top:36px">Menu Links</h5>
  <ul class="abs foot-menu" style="left:390px;top:57px">
    <li>Home</li><li>About Us</li><li>Donation</li><li>Company Profile</li><li>Board Members</li><li>Custom Links</li><li>Contact Us</li>
  </ul>

  <h5 class="abs" style="left:488px;top:36px">News</h5>
  <div class="abs" style="left:488px;top:58px">
    <div class="news-item"><div class="news-thumb" role="img" aria-label="News photo"></div><p>Lorem Ipsum is simply dummy text of the printing and typesetting industry.<small>12 August 2014</small></p></div>
    <div class="news-item"><div class="news-thumb" role="img" aria-label="News photo"></div><p>Lorem Ipsum is simply dummy text of the printing and typesetting industry.<small>12 August 2014</small></p></div>
    <div class="news-item"><div class="news-thumb" role="img" aria-label="News photo"></div><p>Lorem Ipsum is simply dummy text of the printing and typesetting industry.<small>12 August 2014</small></p></div>
  </div>

  <h5 class="abs" style="left:674px;top:36px">Follow Us</h5>
  <div class="abs social" style="left:674px;top:60px" aria-label="Social links"><span></span><span></span><span></span><span></span><span></span></div>
</footer>

</body>
</html>
```